Business Card Design Project - Customized Posters

The project is to design a business card for a new web based company, that designs customized posters celebrating all types of special occasions including birthdays, weddings, new born babys, special memories etc.

You are free to design whatever you want - the only stipulation is the card truly reflects our website and our products. It's preferable that the logo is included (though not essential) and there will be one name and telephone number on the card (use B.Q.Sample as the name and 0987 654321 as the number) as well as our website address and email. The card should be double sided.

Our website is www.novawrenprint.com.au - you will get a complete picture of what we do and hopefully plenty of inspiration for the business card!

Any questions please email sales@novawrenprint.com.au and I'll respond asap. Thanks and good luck!

Target Market(s)

Everyone that would be interested in buying one of our posters!

Industry/Entity Type

Business

Requirements
Must have
• Our website address
Our email address
One name and telephone number
Nice to have
• Our logo
Should not have
• Physical address

```html
<!DOCTYPE html>
<html lang="en">
<head>
<meta charset="utf-8">
<title>Nova Wren Print – Business Card</title>
<link rel="stylesheet" href="https://fonts.googleapis.com/css2?family=Arimo:wght@400;700&display=swap">
<style>
  :root {
    --stage: #2a2a2c;
    --card-white: #ffffff;
    --navy-light: #2f5d95;
    --navy-dark: #173766;
    --maroon-light: #a3121a;
    --maroon-dark: #5e0a0e;
    --line-red: #b0151c;
    --line-yellow: #e4c21a;
    --line-blue: #2f6db3;
    --line-green: #3c8a3a;
    --line-black: #1b1b1b;
    --logo-navy: #2b3088;
    --text-light: #ffffff;
  }
  * { box-sizing: border-box; margin: 0; padding: 0; }
  html, body { width: 1200px; height: 900px; overflow: hidden; }
  body {
    background: var(--stage);
    font-family: "Arimo", Arial, sans-serif;
    display: flex;
    flex-direction: column;
    align-items: center;
    justify-content: center;
    gap: 32px;
  }
  .card {
    position: relative;
    width: 700px;
    height: 400px;
    overflow: hidden;
    background: var(--card-white);
  }

  /* Front side */
  .card-front .photo-collage {
    position: absolute;
    left: 0; top: 0;
    width: 100%; height: 215px;
    background: linear-gradient(100deg, #e8a07a 0%, #d9c2a8 25%, #e7ddd0 50%, #c99880 75%, #e6d6b4 100%);
  }
  .card-front .info-panel {
    position: absolute;
    left: 0; top: 190px;
    width: 100%; height: 150px;
    background: linear-gradient(180deg, var(--navy-light) 0%, var(--navy-dark) 100%);
  }
  .card-front .contact {
    position: absolute;
    left: 390px; top: 150px;
    color: var(--text-light);
    font-size: 19px;
    line-height: 38px;
  }
  .card-front .person-name {
    position: absolute;
    left: 36px; top: 262px;
    color: var(--text-light);
    font-size: 34px;
    font-weight: 400;
  }
  .stripe-set {
    position: absolute;
    left: 0;
    width: 100%;
    display: flex;
    flex-direction: column;
    gap: 5px;
  }
  .stripe { height: 2px; width: 100%; }
  .stripe.red { background: var(--line-red); }
  .stripe.yellow { background: var(--line-yellow); }
  .stripe.blue { background: var(--line-blue); }
  .stripe.green { background: var(--line-green); }
  .stripe.black { background: var(--line-black); }
  .card-front .stripe-set { top: 316px; }

  .footer-band {
    position: absolute;
    left: 0; bottom: 0;
    width: 100%; height: 50px;
    background: linear-gradient(180deg, var(--maroon-light) 0%, var(--maroon-dark) 100%);
    color: var(--text-light);
    font-size: 17px;
    display: flex;
    align-items: center;
    justify-content: center;
    letter-spacing: 0.3px;
  }

  /* Back side */
  .brand {
    position: absolute;
    left: 150px; top: 80px;
    display: flex;
    align-items: center;
    gap: 18px;
  }
  .brand-square {
    width: 64px; height: 64px;
    background: var(--logo-navy);
  }
  .brand-name {
    color: var(--logo-navy);
    font-size: 46px;
    font-weight: 400;
    letter-spacing: 1px;
  }
  .card-back .stripe-set { top: 290px; }
</style>
</head>
<body>

  <section class="card card-front">
    <div class="photo-collage" role="img" aria-label="Collage of celebration photos: birthday cake with candles, balloons, champagne, nursery, friends celebrating and a framed poster"></div>
    <div class="info-panel"></div>
    <div class="contact">
      <p class="contact-phone">Phone : 0987 654321</p>
      <p class="contact-email">E-mail : sales@novawrenprint.com.au</p>
    </div>
    <h1 class="person-name">B.Q.Sample</h1>
    <div class="stripe-set">
      <span class="stripe red"></span>
      <span class="stripe yellow"></span>
      <span class="stripe green"></span>
      <span class="stripe black"></span>
    </div>
    <footer class="footer-band">www.novawrenprint.com.au</footer>
  </section>

  <section class="card card-back">
    <div class="brand">
      <span class="brand-square"></span>
      <span class="brand-name">Nova Wren Print</span>
    </div>
    <div class="stripe-set">
      <span class="stripe red"></span>
      <span class="stripe blue"></span>
      <span class="stripe yellow"></span>
      <span class="stripe green"></span>
      <span class="stripe black"></span>
    </div>
    <footer class="footer-band">www.novawrenprint.com.au</footer>
  </section>

</body>
</html>
```